Business Card Design

Lanternfield Recruitment is a specialist financial services recruitment company and implementation partner

Industry/Entity Type

Business

Contact Information for Business Card

Tom Hadley
Lanternfield Recruiment Ltd
e:tom.hadley@lanternfield-recruitment.example
m:07723 408 316
m:07844 251 903
s: tommhadley

```html
<!DOCTYPE html>
<html lang="en">
<head>
<meta charset="utf-8">
<title>Lanternfield Recruitment – Business Card</title>
<link rel="stylesheet" href="https://fonts.googleapis.com/css2?family=Cinzel:wght@600&family=Tinos&display=swap">
<style>
  :root {
    --page-bg: #e9e7e3;
    --card-white: #ffffff;
    --brand-blue: #0057a8;
    --brand-blue-light: #0a86d6;
    --brand-orange: #f5821f;
    --ink: #1b1b1b;
    --on-blue: #ffffff;
  }
  html, body {
    margin: 0;
    width: 1000px;
    height: 1200px;
    overflow: hidden;
    background: var(--page-bg);
  }
  .canvas { position: relative; width: 1000px; height: 1200px; }
  .card {
    position: absolute;
    width: 783px;
    height: 515px;
    background: var(--card-white);
    overflow: hidden;
    box-shadow: 0 6px 14px rgba(0,0,0,0.25);
  }
  .card--front { left: 112px; top: 73px; }
  .card--back  { left: 114px; top: 633px; }
  .card-art { position: absolute; inset: 0; width: 100%; height: 100%; }

  .holder { position: absolute; left: 46px; top: 42px; color: var(--on-blue); font-family: "Tinos", "Times New Roman", serif; }
  .holder-name { margin: 0; font-size: 33px; font-weight: 400; line-height: 1.1; }
  .holder-role { margin: 0; font-size: 22px; line-height: 1.2; }

  .contacts {
    position: absolute; left: 46px; top: 376px;
    list-style: none; margin: 0; padding: 0;
    color: var(--on-blue);
    font-family: "Tinos", "Times New Roman", serif;
    font-size: 18px;
  }
  .contact { display: flex; align-items: center; height: 25px; }
  .contact-icon { width: 14px; height: 14px; margin-right: 10px; flex: none; }

  .brand { position: absolute; display: flex; align-items: center; }
  .card--front .brand { left: 362px; top: 196px; }
  .card--back .brand { left: 180px; top: 195px; }
  .brand-dot { width: 100px; height: 100px; border-radius: 50%; background: var(--brand-blue); flex: none; margin-right: 14px; }
  .brand-name {
    font-family: "Cinzel", "Times New Roman", serif;
    font-weight: 600;
    font-size: 27px;
    line-height: 1.15;
    color: var(--ink);
    letter-spacing: 0.5px;
  }
</style>
</head>
<body>
<main class="canvas">

  <section class="card card--front" aria-label="Business card front">
    <svg class="card-art" viewBox="0 0 783 515" aria-hidden="true">
      <defs>
        <radialGradient id="blueGlow" cx="180" cy="230" r="360" gradientUnits="userSpaceOnUse">
          <stop offset="0" stop-color="var(--brand-blue-light)"/>
          <stop offset="1" stop-color="var(--brand-blue)"/>
        </radialGradient>
      </defs>
      <path d="M0,0 L290,0 C245,130 268,380 505,515 L0,515 Z" fill="url(#blueGlow)"/>
      <path d="M271,140 C262,330 420,470 630,515 L528,515 C370,450 265,320 271,140 Z" fill="var(--brand-orange)"/>
    </svg>

    <div class="holder">
      <h1 class="holder-name">Tom Hadley</h1>
      <p class="holder-role">Manager</p>
    </div>

    <ul class="contacts">
      <li class="contact">
        <svg class="contact-icon" viewBox="0 0 14 14" aria-hidden="true"><rect x="2.5" y="0.5" width="9" height="13" rx="1.5" fill="none" stroke="currentColor" stroke-width="1.4"/><rect x="4.5" y="2.5" width="5" height="7" fill="currentColor"/></svg>
        07723 408 316
      </li>
      <li class="contact">
        <svg class="contact-icon" viewBox="0 0 14 14" aria-hidden="true"><rect x="2.5" y="0.5" width="9" height="13" rx="1.5" fill="none" stroke="currentColor" stroke-width="1.4"/><rect x="4.5" y="2.5" width="5" height="7" fill="currentColor"/></svg>
        07844 251 903
      </li>
      <li class="contact">
        <svg class="contact-icon" viewBox="0 0 14 14" aria-hidden="true"><circle cx="7" cy="7" r="5" fill="currentColor"/></svg>
        tommhadley
      </li>
      <li class="contact">
        <svg class="contact-icon" viewBox="0 0 14 14" aria-hidden="true"><rect x="0.7" y="2.5" width="12.6" height="9" rx="1" fill="none" stroke="currentColor" stroke-width="1.4"/><path d="M1,3 L7,8 L13,3" fill="none" stroke="currentColor" stroke-width="1.4"/></svg>
        tom.hadley@lanternfield-recruitment.example
      </li>
    </ul>

    <div class="brand">
      <span class="brand-dot" aria-hidden="true"></span>
      <span class="brand-name">LANTERNFIELD<br>RECRUIMENT LTD</span>
    </div>
  </section>

  <section class="card card--back" aria-label="Business card back">
    <svg class="card-art" viewBox="0 0 783 515" aria-hidden="true">
      <path d="M0,282 C40,390 130,470 232,515 L0,515 Z" fill="var(--brand-blue)"/>
      <path d="M2,262 C60,400 220,495 461,515 L330,515 C150,470 40,380 2,262 Z" fill="var(--brand-orange)"/>
    </svg>

    <div class="brand">
      <span class="brand-dot" aria-hidden="true"></span>
      <span class="brand-name">LANTERNFIELD<br>RECRUIMENT LTD</span>
    </div>
  </section>

</main>
</body>
</html>
```